Keelrock Data Partners (KDP) Business Card Design

I would like to create double-sided business cards that contain:
1) Name: Marcus Tolliver
2) Phone Number: +1 (555) 018-2947
3) Email: Marcus.Tolliver@KeelrockDataPartners.com
4) Website: KeelrockDataPartners.com

I would like to include my logo and a color scheme similar to the Vantorra Grand Prix Kelvex team color scheme (black, silver, greenish-blue – but can also include regular blue)

Logos attached.

What we do: Our company develops and delivers innovative and pragmatic information technology and cybersecurity risk and compliance solutions for organizations in the commercial market as well as the federal, and state/local sectors.

```html
<!DOCTYPE html>
<html lang="en">
<head>
<meta charset="utf-8">
<title>Keelrock Data Partners — Business Card</title>
<link rel="stylesheet" href="https://fonts.googleapis.com/css2?family=Montserrat:wght@400;500;700&display=swap">
<style>
  :root {
    --page-bg: #e9ecef;
    --blue-deep: #2f64b3;
    --blue-bright: #3fa8de;
    --accent: #2e8fd8;
    --ink: #1c1c1c;
    --white: #ffffff;
    --card-shadow: rgba(0, 0, 0, 0.18);
  }
  * { box-sizing: border-box; margin: 0; padding: 0; }
  html, body {
    width: 1200px;
    height: 900px;
    overflow: hidden;
    background: var(--page-bg);
    font-family: "Montserrat", sans-serif;
  }
  .sheet {
    width: 1200px;
    height: 900px;
    display: flex;
    flex-direction: column;
    align-items: center;
    justify-content: center;
    gap: 36px;
  }
  .card {
    width: 700px;
    height: 400px;
    border-radius: 26px;
    position: relative;
    overflow: hidden;
    box-shadow: 0 10px 28px var(--card-shadow);
  }

  /* Front side */
  .card-front {
    background: linear-gradient(35deg, var(--blue-deep) 0%, #3479c4 55%, var(--blue-bright) 100%);
    display: flex;
    align-items: center;
    justify-content: center;
  }
  .card-front .glow {
    position: absolute;
    right: -80px;
    top: -90px;
    width: 420px;
    height: 420px;
    border-radius: 50%;
    background: radial-gradient(circle, rgba(255,255,255,0.10) 0%, rgba(255,255,255,0) 70%);
  }
  .brand {
    display: flex;
    align-items: center;
    gap: 22px;
    position: relative;
  }
  .brand-dot {
    width: 86px;
    height: 86px;
    border-radius: 50%;
    border: 6px solid currentColor;
  }
  .brand-name {
    font-weight: 500;
    text-transform: uppercase;
    letter-spacing: 0.08em;
    line-height: 1.02;
  }
  .card-front .brand { color: var(--white); }
  .card-front .brand-name { font-size: 40px; }

  /* Back side */
  .card-back {
    background: var(--white);
    display: flex;
    align-items: center;
    padding: 0 48px 0 52px;
  }
  .card-back .brand { color: var(--accent); gap: 14px; }
  .card-back .brand-dot { width: 52px; height: 52px; border-width: 4px; }
  .card-back .brand-name { font-size: 21px; color: var(--ink); }
  .divider {
    width: 2px;
    height: 130px;
    background: var(--accent);
    margin: 0 30px 0 30px;
    flex-shrink: 0;
  }
  .contact .person {
    font-weight: 700;
    font-size: 30px;
    color: var(--accent);
    line-height: 1.1;
  }
  .contact .role {
    font-size: 17px;
    color: var(--ink);
    margin-bottom: 14px;
  }
  .contact ul { list-style: none; }
  .contact li {
    display: flex;
    align-items: center;
    gap: 10px;
    font-size: 14px;
    color: var(--ink);
    line-height: 1.75;
    white-space: nowrap;
  }
  .contact li.email { font-size: 12.5px; }
  .contact svg { width: 15px; height: 15px; flex-shrink: 0; fill: var(--accent); }
</style>
</head>
<body>
<main class="sheet">
  <section class="card card-front" aria-label="Card front">
    <div class="glow"></div>
    <div class="brand">
      <span class="brand-dot"></span>
      <p class="brand-name">Keelrock<br>Data<br>Partners</p>
    </div>
  </section>

  <section class="card card-back" aria-label="Card back">
    <div class="brand">
      <span class="brand-dot"></span>
      <p class="brand-name">Keelrock<br>Data<br>Partners</p>
    </div>
    <div class="divider"></div>
    <div class="contact">
      <p class="person">Marcus Tolliver</p>
      <p class="role">Owner</p>
      <ul>
        <li class="phone">
          <svg viewBox="0 0 24 24" aria-hidden="true"><path d="M6.6 10.8a15.1 15.1 0 0 0 6.6 6.6l2.2-2.2a1 1 0 0 1 1-.25 11.4 11.4 0 0 0 3.6.57 1 1 0 0 1 1 1V20a1 1 0 0 1-1 1A17 17 0 0 1 3 4a1 1 0 0 1 1-1h3.5a1 1 0 0 1 1 1c0 1.25.2 2.46.57 3.6a1 1 0 0 1-.25 1z"/></svg>
          +1 (555) 018-2947
        </li>
        <li class="email">
          <svg viewBox="0 0 24 24" aria-hidden="true"><path d="M2 5h20v14H2z M3.5 6.5 12 13l8.5-6.5" fill="var(--accent)" stroke="#fff" stroke-width="1.4"/></svg>
          Marcus.Tolliver@KeelrockDataPartners.com
        </li>
        <li class="web">
          <svg viewBox="0 0 24 24" aria-hidden="true"><circle cx="12" cy="12" r="10"/><path d="M2 12h20M12 2c3 3 3 17 0 20M12 2c-3 3-3 17 0 20" fill="none" stroke="#fff" stroke-width="1.3"/></svg>
          KeelrockDataPartners.com
        </li>
      </ul>
    </div>
  </section>
</main>
</body>
</html>
```